Website for IT consulting Company

I need a website upgrade, the existing site content is ok, I would also like to add a testimonial page, the site should be something that is easy for us to update content. You use the content from www.velmarketa.com as an example. I will also post update logo and artwork. I also need a contact form with some type of validation or captcha.

Please omit Address maps

Target Market(s)

small business, service oriented companies. We provide IT Consulting, support and mangement

Industry/Entity Type

Information Technology

Coding

Coded - Design and coding required

Number of Pages Required

1 page

Font styles to use
Serif
Sans Serif

Requirements
Must have
• Contain logo attached, and content from existing web site www.velmarketa.com.
• Also need to update content easily, and be movable to different platforms.
• There is a catch phrase
• "Let us worry about your technology…” “ so you don’t have to!”
• Should be included.
Nice to have
• Testimonial page, Project page where we can post new and past projects and pictures
Should not have
• none

```html
<!DOCTYPE html>
<html lang="en">
<head>
<meta charset="utf-8">
<title>Velmarketa – IT Consulting</title>
<link href="https://fonts.googleapis.com/css2?family=Questrial&family=Open+Sans:wght@400;600;700&display=swap" rel="stylesheet">
<style>
:root{
  --blue:#1e88d4;
  --blue-deep:#1769b0;
  --navy:#233d6b;
  --navy-dark:#1a2c4f;
  --orange:#f47920;
  --ink:#333b46;
  --muted:#6b7380;
  --line:#e3e6ea;
  --light:#f1f2f4;
  --white:#fff;
}
*{box-sizing:border-box;margin:0;padding:0}
html,body{width:1200px;height:3681px;overflow:hidden}
body{position:relative;background:var(--white);font-family:"Open Sans",Arial,sans-serif;color:var(--ink)}
.heading{font-family:"Questrial","Century Gothic",sans-serif;font-weight:400}
.abs{position:absolute}

/* header */
.site-header{position:absolute;left:0;top:0;width:1200px;height:82px;background:var(--white)}
.brand{position:absolute;left:80px;top:18px;display:flex;align-items:center;gap:10px}
.brand-mark{width:26px;height:26px;background:var(--blue)}
.brand-name{font-family:"Questrial",sans-serif;font-size:30px;color:var(--blue);letter-spacing:1px}
.header-phone{position:absolute;right:80px;top:12px;font-size:17px;font-weight:600;color:var(--ink);display:flex;gap:8px;align-items:center}
.main-nav{position:absolute;right:80px;top:44px;display:flex;gap:12px;font-size:14px;color:var(--muted)}
.main-nav .active{color:var(--ink);border-bottom:2px solid var(--blue);padding-bottom:6px}
.main-nav .sep{color:#b8bdc4}

/* hero */
.hero{position:absolute;left:0;top:82px;width:1200px;height:498px;background:linear-gradient(180deg,#5d7595 0%,#3c5478 45%,#2b3f60 100%)}
.hero-title{position:absolute;left:0;width:1200px;top:126px;text-align:center;color:var(--white);font-size:36px;line-height:46px}
.hero-rule{position:absolute;left:530px;top:226px;width:140px;height:1px;background:rgba(255,255,255,.5)}
.hero-sub{position:absolute;left:0;width:1200px;top:250px;text-align:center;color:var(--white);font-size:22px;font-family:"Open Sans",sans-serif;font-weight:600;letter-spacing:.5px}
.hero-points{position:absolute;left:0;width:1200px;top:294px;display:flex;justify-content:center;gap:46px;color:var(--white);font-size:16px}
.hero-points span::before{content:"";display:inline-block;width:9px;height:9px;background:var(--white);transform:rotate(45deg);margin-right:10px}
.btn{display:inline-block;background:var(--orange);color:var(--white);font-weight:700;text-transform:uppercase;text-align:center;border-radius:24px}
.hero-btn{position:absolute;left:490px;top:350px;width:222px;height:46px;line-height:46px;font-size:16px}
.slide-dots{position:absolute;left:1153px;top:200px;display:flex;flex-direction:column;gap:8px}
.slide-dots i{display:block;width:12px;height:12px;border:2px solid var(--blue)}
.slide-dots i.on{background:var(--orange);border-color:var(--orange)}

/* client badges */
.clients{position:absolute;left:0;top:580px;width:1200px;height:97px;background:var(--light);display:flex;align-items:center;justify-content:space-between;padding:0 70px}
.client-badge{width:150px;height:54px;background:#d6dae0;border-radius:4px}
.client-badge.round{width:96px;height:54px;border-radius:50%}
.client-badge.square{width:64px;height:64px}

/* solutions */
.solutions-title{position:absolute;left:78px;top:720px;font-size:34px;line-height:44px;color:var(--ink)}
.solutions-text{position:absolute;left:78px;top:838px;width:530px;font-size:13px;line-height:21px;color:var(--muted)}
.solutions-list{position:absolute;left:78px;top:960px;width:530px;list-style:none;font-size:13px;line-height:20px;color:var(--muted)}
.solutions-list li{display:flex;gap:12px;margin-bottom:14px}
.solutions-list svg{flex:none;margin-top:1px}

.mail-box{position:absolute;left:736px;top:729px;width:300px;height:405px;background:var(--blue);border:6px solid var(--white);box-shadow:0 0 0 1px #cdd9e6;z-index:3;padding:24px 30px}
.mail-box h3{color:var(--white);font-size:17px;font-weight:700}
.mail-box p{color:#dbeaf7;font-size:13px;margin-top:4px}
.field{height:34px;background:var(--white);margin-top:12px;font-size:12px;color:#9aa2ad;padding:9px 10px}
.mail-box .field:first-of-type{margin-top:18px}
.refresh{display:flex;gap:8px;align-items:center;color:var(--white);font-size:13px;margin-top:12px}
.captcha{width:145px;height:50px;margin-top:10px;background:linear-gradient(90deg,#d3d6da,#eceef0,#c9ccd0)}
.mail-submit{position:absolute;left:788px;top:1110px;width:196px;height:44px;line-height:44px;font-size:15px;z-index:4}

/* training */
.training{position:absolute;left:0;top:1134px;width:1200px;height:621px;background:linear-gradient(135deg,#2a74c4 0%,#1c5fae 100%);clip-path:polygon(0 15%,100% 0,100% 100%,0 100%)}
.training-title{position:absolute;left:0;width:1200px;top:1226px;text-align:center;color:var(--white);font-size:34px}
.title-rule{position:absolute;width:120px;height:2px;left:540px}
.training .rings{position:absolute;left:142px;top:225px;width:300px;height:300px;border:1px solid rgba(255,255,255,.25);border-radius:50%}
.training .rings2{position:absolute;left:172px;top:255px;width:240px;height:240px;border:1px solid rgba(255,255,255,.2);border-radius:50%}
.trainer-photo{position:absolute;left:230px;top:1370px;width:165px;height:385px;background:linear-gradient(180deg,#e9eef4 0%,#c8d3e0 50%,#3a4660 100%);border-radius:80px 80px 0 0}
.training-intro{position:absolute;left:600px;top:1306px;width:520px;color:var(--white);font-size:16px;line-height:24px}
.method{position:absolute;left:596px;width:540px;display:flex;gap:18px}
.method-icon{flex:none;width:70px;height:70px;border-radius:50%;background:var(--white);display:flex;align-items:center;justify-content:center}
.method h4{color:var(--white);font-size:15px;font-weight:700;margin-top:6px}
.method p{color:#d9e7f6;font-size:12px;line-height:18px;margin-top:4px}

/* projects */
.section-title{position:absolute;left:0;width:1200px;text-align:center;font-size:34px;color:var(--ink)}
.project{position:absolute;width:231px;height:204px;background:var(--white);box-shadow:0 2px 6px rgba(0,0,0,.12)}
.project-photo{height:140px;background:linear-gradient(135deg,#b9c9db,#6f86a3)}
.project p{padding:12px 14px;font-size:11px;line-height:17px;color:var(--muted)}

/* about */
.about{position:absolute;left:0;top:2380px;width:1200px;height:491px;background:linear-gradient(135deg,#3d5f92 0%,#2b4a7c 100%);clip-path:polygon(0 0,100% 14%,100% 100%,0 100%)}
.about-title{position:absolute;left:0;width:1200px;top:2488px;text-align:center;color:var(--white);font-size:34px}
.about-lead{position:absolute;left:78px;top:2566px;width:530px;color:var(--white);font-size:18px;line-height:27px}
.about-text{position:absolute;left:78px;top:2632px;width:535px;color:#dbe4f0;font-size:12.5px;line-height:20px}
.read-more{position:absolute;left:78px;top:2806px;color:var(--white);font-size:13px}
.video{position:absolute;left:655px;top:2574px;width:464px;height:246px;background:linear-gradient(135deg,#2b3444,#151b26);display:flex;align-items:center;justify-content:center}
.video-name{position:absolute;left:90px;top:150px;font-family:"Questrial",sans-serif;font-size:40px;color:var(--white);letter-spacing:1px}
.play{position:absolute;left:198px;top:52px}

/* testimonials */
.quote-card{position:absolute;top:3026px;width:319px;height:127px;background:var(--light);padding:20px 22px 0 68px;font-size:12.5px;line-height:19px;font-style:italic;color:var(--muted)}
.quote-card::before{content:"\201C";position:absolute;left:18px;top:-4px;font-family:Georgia,serif;font-size:70px;font-style:normal;color:var(--blue)}
.quote-card::after{content:"";position:absolute;left:152px;bottom:-10px;border-left:10px solid transparent;border-right:10px solid transparent;border-top:10px solid var(--light)}
.avatar{position:absolute;top:3190px;width:60px;height:60px;border-radius:50%;border:3px solid var(--blue);background:linear-gradient(180deg,#dfe5ec,#7b8aa0)}
.client-name{position:absolute;top:3259px;width:140px;text-align:center;font-size:12px;font-weight:600;color:var(--ink)}

/* footer */
.site-footer{position:absolute;left:0;top:3325px;width:1200px;height:356px;background:linear-gradient(135deg,#2a86d2,#1b6fbd)}
.footer-brand{position:absolute;left:80px;top:76px;display:flex;gap:10px;align-items:center}
.footer-brand .brand-mark{background:var(--white)}
.footer-brand .brand-name{color:var(--white)}
.footer-about{position:absolute;left:80px;top:140px;width:215px;font-size:12px;line-height:19px;color:var(--white)}
.footer-links{position:absolute;left:378px;top:82px;list-style:none;font-size:13px;line-height:20px;color:var(--white)}
.footer-contact{position:absolute;left:600px;top:82px;font-size:12.5px;line-height:18px;color:var(--white)}
.footer-contact .row{display:flex;gap:32px;margin-bottom:16px}
.footer-contact .label{width:60px}
.footer-divider{width:250px;height:1px;background:rgba(255,255,255,.35);margin:-4px 0 14px}
.socials{display:flex;gap:8px}
.socials i{display:block;width:22px;height:22px;border:1px solid var(--white)}
.newsletter{position:absolute;left:932px;top:82px;color:var(--white);font-size:13px;font-weight:600}
.newsletter .input{margin-top:16px;width:185px;height:40px;background:var(--orange);display:flex;align-items:center;justify-content:space-between;padding:0 12px;font-size:12px;font-weight:400;color:#ffe4cf}
.footer-bar{position:absolute;left:80px;top:282px;width:1040px;height:1px;background:rgba(255,255,255,.35)}
.copyright{position:absolute;left:80px;top:307px;font-size:12px;color:var(--white)}
.terms{position:absolute;right:80px;top:307px;font-size:12px;color:var(--white)}
</style>
</head>
<body>

<header class="site-header">
  <div class="brand"><span class="brand-mark"></span><span class="brand-name">Velmarketa</span></div>
  <div class="header-phone">
    <svg width="14" height="14" viewBox="0 0 24 24"><path fill="#1e88d4" d="M6.6 10.8a15 15 0 0 0 6.6 6.6l2.2-2.2c.3-.3.7-.4 1-.2 1.1.4 2.3.6 3.6.6.6 0 1 .4 1 1V20c0 .6-.4 1-1 1A17 17 0 0 1 3 4c0-.6.4-1 1-1h3.5c.6 0 1 .4 1 1 0 1.3.2 2.5.6 3.6.1.3 0 .7-.2 1z"/></svg>
    800.555.0142
  </div>
  <nav class="main-nav"><span class="active">About</span><span class="sep">/</span><span>Blog</span><span class="sep">/</span><span>Workshops</span><span class="sep">/</span><span>Contact</span></nav>
</header>

<section class="hero" role="img" aria-label="Photo of a team working together at laptops, under a dark blue overlay">
  <h1 class="hero-title heading">For over 40 years, Crestline Training has helped<br>people in organizations perform better together.</h1>
  <div class="hero-rule"></div>
  <div class="hero-sub">3 Productivty Outcomes</div>
  <div class="hero-points"><span>More Done In Less Time</span><span>Graeter Engagement</span><span>Better Results</span></div>
  <span class="btn hero-btn">Learn More</span>
  <div class="slide-dots"><i class="on"></i><i></i><i></i></div>
</section>

<div class="clients">
  <span class="client-badge square"></span>
  <span class="client-badge" style="width:230px"></span>
  <span class="client-badge" style="width:120px"></span>
  <span class="client-badge round"></span>
  <span class="client-badge" style="width:130px"></span>
</div>

<h2 class="solutions-title heading">flexible solutions for your<br>business needs</h2>
<p class="solutions-text">Velmarketa is a technology solution provider based in Houston, Texas. Our goal is to make technology a non-issue for individuals and small to medium size businesses ranging from 5 to 150 Users. Velmarketa has the experience, the tools, high-level technology solutions and training to power your business and your work force. We understand that all business's have one goal in common!</p>
<ul class="solutions-list">
  <li><svg width="16" height="16" viewBox="0 0 16 16"><circle cx="8" cy="8" r="7" fill="none" stroke="#1e88d4" stroke-width="1.4"/><path d="M5 8h6M8.5 5.5 11 8l-2.5 2.5" fill="none" stroke="#1e88d4" stroke-width="1.4"/></svg>We work with managers and trainers because their roles enable them to multiply the success of others.</li>
  <li><svg width="16" height="16" viewBox="0 0 16 16"><circle cx="8" cy="8" r="7" fill="none" stroke="#1e88d4" stroke-width="1.4"/><path d="M5 8h6M8.5 5.5 11 8l-2.5 2.5" fill="none" stroke="#1e88d4" stroke-width="1.4"/></svg>We focus on people skills because improving interpersonal interactions is the quickest and cheapest way to accelerate employee engagement and performance.</li>
  <li><svg width="16" height="16" viewBox="0 0 16 16"><circle cx="8" cy="8" r="7" fill="none" stroke="#1e88d4" stroke-width="1.4"/><path d="M5 8h6M8.5 5.5 11 8l-2.5 2.5" fill="none" stroke="#1e88d4" stroke-width="1.4"/></svg>We certify client trainers to embed the skills in their organizations.</li>
</ul>

<form class="mail-box">
  <h3>Join Our Mailing List</h3>
  <p>Get Our Latest Thinking and more</p>
  <div class="field">Name</div>
  <div class="field">Email</div>
  <div class="field">Contact number</div>
  <div class="field">Enter captcha</div>
  <div class="refresh"><svg width="16" height="16" viewBox="0 0 16 16"><path d="M13 8a5 5 0 1 1-1.5-3.6M13 2v3h-3" fill="none" stroke="#fff" stroke-width="1.5"/></svg>Refresh captcha</div>
  <div class="captcha" role="img" aria-label="Distorted captcha characters"></div>
</form>
<span class="btn mail-submit">Submit</span>

<section class="training">
  <div class="rings"></div><div class="rings2"></div>
</section>
<h2 class="training-title heading">Training Method</h2>
<div class="title-rule" style="top:1276px;background:rgba(255,255,255,.5)"></div>
<div class="trainer-photo" role="img" aria-label="Photo of a smiling trainer standing with hands on hips"></div>
<p class="training-intro">To assure excellence in every workshop, each course shares the same foundational characteristics:</p>

<div class="method" style="top:1368px">
  <div class="method-icon"><svg width="30" height="30" viewBox="0 0 30 30"><path d="M8 22 22 8M8 8l14 14" stroke="#1e6bbf" stroke-width="3"/></svg></div>
  <div><h4>PRACTICE-DRIVEN</h4><p>For participants to be successful on the job, they must first be successful in the workshop.</p></div>
</div>
<div class="method" style="top:1456px">
  <div class="method-icon"><svg width="30" height="30" viewBox="0 0 30 30"><rect x="4" y="6" width="22" height="15" fill="none" stroke="#1e6bbf" stroke-width="2.5"/><path d="M11 25h8" stroke="#1e6bbf" stroke-width="2.5"/></svg></div>
  <div><h4>PERSONALIZED</h4><p>Participants practice skills using their own "real-play" scenarios versus generic role-plays scripted in advance.</p></div>
</div>
<div class="method" style="top:1544px">
  <div class="method-icon"><svg width="30" height="30" viewBox="0 0 30 30"><path d="M15 3 25 7v8c0 6-4 10-10 12C9 25 5 21 5 15V7z" fill="#1e6bbf"/><path d="m10 15 3.5 3.5L20 12" fill="none" stroke="#fff" stroke-width="2.5"/></svg></div>
  <div><h4>AUTHENTIC</h4><p>Participants practice skills using their own "real-play" scenarios versus generic role-plays scripted in advance.</p></div>
</div>
<div class="method" style="top:1632px">
  <div class="method-icon"><svg width="30" height="30" viewBox="0 0 30 30"><rect x="5" y="5" width="20" height="20" fill="none" stroke="#1e6bbf" stroke-width="2.5"/><path d="M11 11h8v8" fill="none" stroke="#1e6bbf" stroke-width="2.5"/></svg></div>
  <div><h4>INTEGRATED</h4><p>Participants practice skills using their own "real-play" scenarios versus generic role-plays scripted in advance.</p></div>
</div>

<h2 class="section-title heading" style="top:1806px">Latest Projects</h2>
<div class="title-rule" style="top:1856px;background:var(--line)"></div>

<article class="project" style="left:133px;top:1914px"><div class="project-photo" role="img" aria-label="Photo of hands reviewing charts on paper"></div><p>Sed ut perspiciatis unde omnis iste natus</p></article>
<article class="project" style="left:486px;top:1914px"><div class="project-photo" role="img" aria-label="Photo of a team in a meeting room"></div><p>Sed ut perspiciatis unde omnis iste natus</p></article>
<article class="project" style="left:837px;top:1914px"><div class="project-photo" role="img" aria-label="Photo of a group of business people"></div><p>Sed ut perspiciatis unde omnis iste natus</p></article>
<article class="project" style="left:133px;top:2138px"><div class="project-photo" role="img" aria-label="Photo of a workshop discussion"></div><p>Sed ut perspiciatis unde omnis iste natus</p></article>
<article class="project" style="left:486px;top:2138px"><div class="project-photo" role="img" aria-label="Photo of colleagues reviewing documents"></div><p>Sed ut perspiciatis unde omnis iste natus</p></article>
<article class="project" style="left:837px;top:2138px"><div class="project-photo" role="img" aria-label="Photo of a team collaborating at a table"></div><p>Sed ut perspiciatis unde omnis iste natus</p></article>

<section class="about" role="img" aria-label="Photo of people at work under a blue overlay"></section>
<h2 class="about-title heading">Know More About Us</h2>
<div class="title-rule" style="top:2538px;background:rgba(255,255,255,.5)"></div>
<p class="about-lead">We teach managers and trainers the people skills they need to 2X their success.</p>
<p class="about-text">We work with managers and trainers because their roles enable them to multiply the success of others. We focus on people skills because improving interpersonal interactions is the quickest and cheapest way to accelerate employee engagement and performance. We certify client trainers to embed the skills in their organizations. Our workshops are small-group master classes. Participants practice the skills using their real work issues and get coached by master trainers in real-time.Participants leave able to start 2Xing their success the very next day.</p>
<span class="read-more">Read More</span>
<div class="video" role="img" aria-label="Video thumbnail with a play button">
  <svg class="play" width="68" height="68" viewBox="0 0 68 68"><circle cx="34" cy="34" r="31" fill="none" stroke="#f47920" stroke-width="4"/><path d="M27 21v26l20-13z" fill="#f47920"/></svg>
  <span class="video-name">Velmarketa</span>
</div>

<h2 class="section-title heading" style="top:2920px">Some Impressions From Our Customers !</h2>
<div class="title-rule" style="top:2972px;background:var(--line)"></div>

<blockquote class="quote-card" style="left:80px">Neque porro quisquam est, qui dolorem ipsum quia dolor sit amet, consectetur, adipisci velit, sed quia</blockquote>
<blockquote class="quote-card" style="left:441px">Neque porro quisquam est, qui dolorem ipsum quia dolor sit amet, consectetur, adipisci velit, sed quia</blockquote>
<blockquote class="quote-card" style="left:802px">Neque porro quisquam est, qui dolorem ipsum quia dolor sit amet, consectetur, adipisci velit, sed quia</blockquote>
<div class="avatar" role="img" aria-label="Customer portrait" style="left:178px"></div>
<div class="avatar" role="img" aria-label="Customer portrait" style="left:539px"></div>
<div class="avatar" role="img" aria-label="Customer portrait" style="left:900px"></div>
<div class="client-name" style="left:138px">LENA MORROW</div>
<div class="client-name" style="left:499px">LENA MORROW</div>
<div class="client-name" style="left:860px">LENA MORROW</div>

<footer class="site-footer">
  <div class="footer-brand"><span class="brand-mark"></span><span class="brand-name">Velmarketa</span></div>
  <p class="footer-about">Sed ut perspiciatis unde omnis iste natus error sit voluptatem accusan tium doloremque laudantium</p>
  <ul class="footer-links"><li>Home</li><li>About</li><li>Blog</li><li>Workshops</li><li>Contact</li></ul>
  <div class="footer-contact">
    <div class="row"><span class="label">Address :</span><span>Northgate Inc.<br>118 Harbor Lane, Suite 200<br>Oakland, CA 94607</span></div>
    <div class="row"><span class="label">Mobile No:</span><span>800.555.0142</span></div>
    <div class="footer-divider"></div>
    <div class="row" style="align-items:center"><span class="label">Follow Us:</span><span class="socials"><i></i><i></i><i></i><i></i></span></div>
  </div>
  <div class="newsletter">Subscribe Us For Latest News
    <div class="input">Enter Email<svg width="14" height="10" viewBox="0 0 14 10"><path d="M0 5h12M8 1l4 4-4 4" fill="none" stroke="#fff" stroke-width="1.5"/></svg></div>
  </div>
  <div class="footer-bar"></div>
  <span class="copyright">COPYRIGHT © 2017 ALL RIGHT RESERVED</span>
  <span class="terms">TERMS &amp; CONDITIONS</span>
</footer>

</body>
</html>
```